Summer Special for Harbourline Gym

Running a 12 month special starting from 1st Jan 2019. I already have the image (see below), I just need the font and layout to have a summer feel and to be eye catching. Format required is for a Facebook cover, Instagram, if possible the one image but spread across 3 tiles on the homepage and a format for a poster .

"SUMMER SPECIAL
12 months from
$350.00
SAVE OVER 20%"
"Terms and conditions apply"

Attached is the photo for the current promo, a logo we generally use and another special we have run in the past to assist you

Target Market(s)

18 - 45 male and female

Industry/Entity Type

Fitness

Font styles to use
Sans Serif
Script

Colors

Designer to choose colors to be used in the design.

Requirements
Must have
• The main emphasis would be on the Summer font/text (special) and the layout of the text. If we can add some brighter colors to the layout that would be great just to capture their attention. If there's any effects you want to add to it that would be great. The logo can be faint in the background.
• "SUMMER SPECIAL
• 12 months from
• $350.00
• SAVE OVER 20%"
• "Terms and conditions apply"
• All contact details, address, website, etc which will be supplied
Nice to have
• Some artistic effects to catch your eye and enhance the professionalism of the designer

```html
<!DOCTYPE html>
<html lang="en">
<head>
<meta charset="utf-8">
<title>Harbourline Gym – Summer Special</title>
<link href="https://fonts.googleapis.com/css2?family=Russo+One&family=Oswald:wght@400;500;700&family=Montserrat:wght@400&display=swap" rel="stylesheet">
<style>
:root{
  --board:#6b6c6e;
  --sky:#e3e9ec;
  --sky-deep:#c9d9e3;
  --wave:#a9cde2;
  --ink:#141414;
  --banner:#0d0d0d;
  --gold-1:#ffe259;
  --gold-2:#f7a81b;
  --accent-yellow:#f6b814;
  --red:#d52a1e;
  --red-dark:#9e1510;
  --price:#d8261b;
  --white:#ffffff;
  --label:#f2f2f2;
}
*{margin:0;padding:0;box-sizing:border-box}
html,body{width:1200px;height:933px;overflow:hidden}
body{background:var(--board);position:relative;font-family:"Oswald",sans-serif}

.artboard{position:absolute;overflow:hidden;
  background:linear-gradient(160deg,var(--white) 0%,var(--sky) 45%,var(--sky-deep) 100%)}
.artboard--facebook{left:32px;top:42px;width:516px;height:243px}
.artboard--instagram{left:30px;top:346px;width:518px;height:516px}
.artboard--poster{left:581px;top:42px;width:581px;height:822px}

.format-label{position:absolute;font-family:"Montserrat",sans-serif;font-size:18px;color:var(--label);transform:translateX(-50%)}

.wave{position:absolute;border-radius:50%;background:var(--wave);opacity:.7}
.line-art{position:absolute;inset:0;width:100%;height:100%}
.palms{position:absolute;border-radius:50% 50% 40% 40%;
  background:radial-gradient(ellipse at 50% 70%,#3f7a2c 0%,#2f6a22 45%,rgba(47,106,34,0) 72%)}
.athlete{position:absolute;border-radius:45% 45% 0 0;
  background:linear-gradient(180deg,#1c1c22 0%,#1c1c22 12%,#6b3b26 22%,#b4694a 45%,#8a4a32 62%,#e0684a 72%,#f07a22 100%)}
.headline{position:absolute}
.offer{position:absolute;color:var(--ink);text-align:center;line-height:1.15;font-weight:500}
.offer .price{color:var(--price)}
.save-bar{position:absolute;left:0;background:var(--red);color:var(--white);
  clip-path:polygon(0 0,100% 0,94% 100%,0 100%);display:flex;align-items:center;justify-content:center;font-weight:500}
.contact{position:absolute;color:var(--ink);line-height:1.45;text-align:center;font-weight:400}
.terms-badge{position:absolute;border-radius:50%;color:var(--white);
  background:radial-gradient(circle at 45% 35%,#e8473a 0%,var(--red) 50%,var(--red-dark) 100%);
  box-shadow:0 3px 8px rgba(0,0,0,.35);border:2px solid rgba(255,255,255,.6);
  display:flex;align-items:center;justify-content:center;text-align:center;font-weight:500;line-height:1.2}
.brand{position:absolute;font-family:"Oswald",sans-serif;font-weight:700;color:var(--ink);white-space:nowrap;letter-spacing:.02em}
</style>
</head>
<body>

<svg width="0" height="0" style="position:absolute" aria-hidden="true">
  <defs>
    <linearGradient id="gold" x1="0" y1="0" x2="0" y2="1">
      <stop offset="0" stop-color="var(--gold-1)"/>
      <stop offset="1" stop-color="var(--gold-2)"/>
    </linearGradient>
  </defs>
</svg>

<!-- Facebook cover -->
<section class="artboard artboard--facebook">
  <div class="wave" style="left:-60px;top:150px;width:300px;height:160px"></div>
  <svg class="line-art" viewBox="0 0 516 243" aria-hidden="true">
    <g fill="none" stroke="var(--white)" stroke-width="1.5" opacity=".9">
      <polygon points="20,30 290,30 160,235"/>
      <polygon points="330,20 480,243 180,243"/>
    </g>
  </svg>
  <div class="palms" role="img" aria-label="Palm fronds" style="left:48px;top:6px;width:256px;height:96px"></div>
  <div class="athlete" role="img" aria-label="Photo of a muscular man in a cap and orange shorts" style="left:356px;top:6px;width:160px;height:237px"></div>
  <svg class="headline" viewBox="0 0 380 180" style="left:0;top:72px;width:293px;height:139px">
    <polygon points="125,8 365,40 290,176 160,176" fill="var(--accent-yellow)"/>
    <polygon points="0,28 355,28 325,152 0,152" fill="var(--banner)"/>
    <g font-family="Russo One, sans-serif" fill="url(#gold)" font-size="56" text-anchor="middle">
      <text x="172" y="88" textLength="300" lengthAdjust="spacingAndGlyphs">SUMMER</text>
      <text x="166" y="142" textLength="270" lengthAdjust="spacingAndGlyphs">SPECIAL</text>
    </g>
  </svg>
  <div class="offer" style="right:168px;top:146px;font-size:16px;text-align:right">12 MONTHS<br>FROM <span class="price">$350.00</span></div>
  <div class="save-bar" style="left:238px;top:189px;width:122px;height:21px;font-size:15px">SAVE OVER 20%</div>
  <div class="contact" style="right:161px;top:220px;font-size:6.5px;text-align:right">14 Pier Road, Dockside Bay Victoria 3050<br>hello@harbourlinegym.com.au | www.harbourlinegym.com.au</div>
  <div class="brand" style="left:10px;top:205px;font-size:13px">HARBOURLINE GYM</div>
  <div class="terms-badge" style="left:458px;top:10px;width:48px;height:48px;font-size:7px">Terms and<br>conditions<br>apply</div>
</section>
<div class="format-label" style="left:284px;top:304px">Facebook</div>

<!-- Instagram -->
<section class="artboard artboard--instagram">
  <div class="wave" style="left:-80px;top:380px;width:480px;height:260px"></div>
  <svg class="line-art" viewBox="0 0 518 516" aria-hidden="true">
    <g fill="none" stroke="var(--white)" stroke-width="2" opacity=".9">
      <polygon points="10,250 330,250 170,500"/>
      <polygon points="330,30 518,330 200,330"/>
    </g>
  </svg>
  <div class="palms" role="img" aria-label="Palm fronds" style="left:58px;top:6px;width:312px;height:124px"></div>
  <div class="athlete" role="img" aria-label="Photo of a muscular man in a cap and orange shorts" style="left:302px;top:14px;width:216px;height:502px"></div>
  <svg class="headline" viewBox="0 0 380 180" style="left:0;top:86px;width:350px;height:166px">
    <polygon points="125,8 365,40 290,176 160,176" fill="var(--accent-yellow)"/>
    <polygon points="0,28 355,28 325,152 0,152" fill="var(--banner)"/>
    <g font-family="Russo One, sans-serif" fill="url(#gold)" font-size="56" text-anchor="middle">
      <text x="172" y="88" textLength="300" lengthAdjust="spacingAndGlyphs">SUMMER</text>
      <text x="166" y="142" textLength="270" lengthAdjust="spacingAndGlyphs">SPECIAL</text>
    </g>
  </svg>
  <div class="offer" style="left:40px;width:210px;top:274px;font-size:26px">12 MONTHS<br>FROM <span class="price">$350.00</span></div>
  <div class="save-bar" style="top:339px;width:264px;height:41px;font-size:27px">SAVE OVER 20%</div>
  <div class="contact" style="left:10px;width:320px;top:386px;font-size:11.5px">14 Pier Road, Dockside Bay Victoria 3050<br>hello@harbourlinegym.com.au | www.harbourlinegym.com.au</div>
  <div class="brand" style="left:18px;top:458px;font-size:19px">HARBOURLINE GYM</div>
  <div class="terms-badge" style="left:446px;top:16px;width:58px;height:58px;font-size:9px">Terms and<br>conditions<br>apply</div>
</section>
<div class="format-label" style="left:282px;top:888px">Instagram</div>

<!-- Poster -->
<section class="artboard artboard--poster">
  <div class="wave" style="left:-120px;top:590px;width:620px;height:340px"></div>
  <svg class="line-art" viewBox="0 0 581 822" aria-hidden="true">
    <g fill="none" stroke="var(--white)" stroke-width="2.5" opacity=".9">
      <polyline points="0,330 300,330 120,680"/>
      <polygon points="380,200 581,520 200,520"/>
      <polyline points="0,500 40,560 0,620"/>
    </g>
  </svg>
  <div class="palms" role="img" aria-label="Palm fronds" style="left:75px;top:22px;width:336px;height:124px"></div>
  <div class="athlete" role="img" aria-label="Photo of a muscular man in a cap and orange shorts" style="left:267px;top:38px;width:314px;height:784px"></div>
  <svg class="headline" viewBox="0 0 380 180" style="left:0;top:110px;width:380px;height:180px">
    <polygon points="125,8 365,40 290,176 160,176" fill="var(--accent-yellow)"/>
    <polygon points="0,28 355,28 325,152 0,152" fill="var(--banner)"/>
    <g font-family="Russo One, sans-serif" fill="url(#gold)" font-size="56" text-anchor="middle">
      <text x="172" y="88" textLength="300" lengthAdjust="spacingAndGlyphs">SUMMER</text>
      <text x="166" y="142" textLength="270" lengthAdjust="spacingAndGlyphs">SPECIAL</text>
    </g>
  </svg>
  <div class="offer" style="left:30px;width:210px;top:358px;font-size:28px">12 MONTHS<br>FROM <span class="price">$350.00</span></div>
  <div class="save-bar" style="top:426px;width:256px;height:42px;font-size:28px">SAVE OVER 20%</div>
  <div class="contact" style="left:0;width:300px;top:475px;font-size:12px">14 Pier Road, Dockside Bay Victoria 3050<br>hello@harbourlinegym.com.au | www.harbourlinegym.com.au</div>
  <div class="terms-badge" style="left:69px;top:530px;width:136px;height:136px;font-size:21px">Terms and<br>conditions<br>apply</div>
  <div class="brand" style="left:31px;top:714px;font-size:31px">HARBOURLINE GYM</div>
</section>
<div class="format-label" style="left:863px;top:880px">Poster</div>

</body>
</html>
```